Business Card Design

No logos or construction designs

Easy to read Ray Tolliver Roofing, LLC (in red)

all other lettering in black I guess I am open to what the designers come up

Industry/Entity Type

Construction

Contact Information for Business Card

Ray Tolliver Roofing, LLC office 555-2189063 fax 555-318-940 3075 Marrowfield W Brenwick, Calder State 40000
Ray@RayTolliverRoofing.example Residential Commerical
Ray Tolliver cell 555-862-1375

```html
<!DOCTYPE html>
<html lang="en">
<head>
<meta charset="utf-8">
<title>Ray Tolliver Roofing, LLC – Business Card</title>
<link href="https://fonts.googleapis.com/css2?family=Cinzel:wght@400;600&family=Open+Sans:wght@400&display=swap" rel="stylesheet">
<style>
  :root{
    --backdrop:#3b3b3b;
    --backdrop-light:#555555;
    --card-black:#0c0c0c;
    --roof-red:#6e0508;
    --roof-red-light:#8c171b;
    --paper:#ffffff;
    --paper-shade:#e9e9e9;
    --rule:#f3f3f3;
    --ink:#111111;
    --icon-red:#7a0a0c;
    --title:#f4f4f4;
  }
  *{margin:0;padding:0;box-sizing:border-box;}
  html,body{width:1200px;height:900px;overflow:hidden;}
  body{
    background:radial-gradient(ellipse at 50% 40%, var(--backdrop-light), var(--backdrop) 70%);
    position:relative;
  }
  .business-card{
    position:absolute;left:100px;top:164px;width:1000px;height:572px;
    background:var(--card-black);border-radius:6px;overflow:hidden;
    box-shadow:0 18px 40px rgba(0,0,0,.45);
  }
  .header-band{
    position:absolute;left:0;top:22px;width:100%;height:228px;
    background:linear-gradient(100deg,var(--roof-red) 0%,var(--roof-red-light) 55%,var(--roof-red) 100%);
  }
  .header-band::before{
    content:"";position:absolute;left:0;right:0;top:8px;height:2px;background:var(--rule);
  }
  .contact-panel{
    position:absolute;left:0;top:250px;width:100%;height:250px;
    background:linear-gradient(160deg,var(--paper) 40%,var(--paper-shade) 100%);
  }
  .footer-band{
    position:absolute;left:0;top:500px;width:100%;height:40px;background:var(--roof-red);
  }
  .footer-band::after{
    content:"";position:absolute;left:0;right:0;top:10px;height:2px;background:var(--rule);
  }
  .side-tab{position:absolute;width:46px;background:var(--card-black);border-radius:18px;}
  .side-tab--left{left:-22px;top:268px;height:196px;}
  .side-tab--right{right:-22px;top:346px;height:160px;}
  .company-name{
    position:absolute;left:86px;top:58px;color:var(--title);
    font-family:"Cinzel",serif;text-shadow:0 1px 2px rgba(0,0,0,.35);
  }
  .company-name__owner{display:block;font-size:74px;font-weight:600;line-height:1;letter-spacing:1px;}
  .company-name__trade{display:block;font-size:44px;font-weight:400;line-height:1.2;margin-top:4px;}
  .contact-list{
    position:absolute;left:52px;top:298px;list-style:none;
    font-family:"Open Sans",sans-serif;font-size:24px;color:var(--ink);
  }
  .contact-list li{display:flex;align-items:center;height:36px;gap:12px;}
  .contact-list svg{width:22px;height:22px;fill:var(--icon-red);flex:none;}
  .address{
    position:absolute;right:80px;top:410px;text-align:right;font-style:normal;
    font-family:"Open Sans",sans-serif;font-size:24px;line-height:34px;color:var(--ink);
  }
</style>
</head>
<body>
  <article class="business-card">
    <div class="header-band"></div>
    <div class="contact-panel"></div>
    <div class="footer-band"></div>
    <div class="side-tab side-tab--left"></div>
    <div class="side-tab side-tab--right"></div>

    <h1 class="company-name">
      <span class="company-name__owner">Ray Tolliver</span>
      <span class="company-name__trade">Roofing, LLC</span>
    </h1>

    <ul class="contact-list">
      <li>
        <svg viewBox="0 0 24 24" aria-label="Office phone"><path d="M6.6 2.5l3 3.2-1.8 2.4c1.2 2.8 3.3 5 6.1 6.2l2.4-1.8 3.2 3-1.6 3.6c-8.6-.5-14.4-6.3-14.9-14.9z"/></svg>
        <span>555-2189063</span>
      </li>
      <li>
        <svg viewBox="0 0 24 24" aria-label="Fax"><path d="M7 2h8l3 3v6H7zM4 11h16a2 2 0 0 1 2 2v8H2v-8a2 2 0 0 1 2-2zm3 4v2h10v-2z"/></svg>
        <span>555-318-940</span>
      </li>
      <li>
        <svg viewBox="0 0 24 24" aria-label="Cell phone"><path d="M8 1h2v3h4a2 2 0 0 1 2 2v15a2 2 0 0 1-2 2H8a2 2 0 0 1-2-2V6a2 2 0 0 1 2-2zm0 6v5h8V7z"/></svg>
        <span>555-862-1375</span>
      </li>
      <li>
        <svg viewBox="0 0 24 24" aria-label="Email"><path d="M2 5h20v14H2zm2 2v.6l8 5.4 8-5.4V7z"/></svg>
        <span>Ray@RayTolliverRoofing.example</span>
      </li>
    </ul>

    <address class="address">
      3075 Marrowfield W Brenwick<br>
      Calder State 40000
    </address>
  </article>
</body>
</html>
```